Marijuana Lifestyle Multi-Shop Brand Website

We need a website that provides an online retail shop for our products, along with the additional functionality:

Main Page: Slider with great photography (we are still looking for a professional photographer to take photos for us.

Shop Tab: E-commerce site.
- Main Categories:
- Accessories
- Bubblers
- Dry Pieces
- Scientific Glass
- Water Pipes
- Custom Shop
- University Store

Stores/Resellers: This is a store look-up, so people can enter their zipcode and find our resellers and partners.

Brand Partners: Just a basic filter and page so that we can highlight our partners and why we've selected them.

Contact Us: Basic Form
- Career Page: Basic Page

About Us: Basic Page

Blog:

Search Bar:

Essentially, we want a near exact copy of this website, but with our brand, logo and content. https://corkwillowbins.com/

This site is really really simple, but we like simple.

Our reserved domain address is: www.runbaketend.com

About Us:
We are multi-shop for marijuana-related accessories. We sell quality glass pipes, vaporizers, amazing storage options, dime bags, custom t-shirts and other stuff.

We have a network of resellers that allow us to put in micro-installations into gift shops, convenience stores, tobacco stores, etc. and we are trying to change the overall perception that buying these items should be mainstream and as transparent as going to the Fen or the Walnut Shop.

I've attached a logo that should give you an idea of our color scheme. We don't have our photography yet for the slider
Updates

As an FYI, for the e-commerce part of my website, I already have a license for WP SwiftTill.

Industry/Entity Type

Shop

```html
<!DOCTYPE html>
<html lang="en">
<head>
<meta charset="utf-8">
<title>About Us – Birch Self</title>
<link rel="stylesheet" href="https://fonts.googleapis.com/css2?family=Barlow+Semi+Condensed:wght@400;500;600;700&display=swap">
<style>
  :root {
    --olive-dark: #44531c;
    --olive-top: #5d6b33;
    --nav-green: #b9cb8d;
    --page-bg: #dfe3c6;
    --ink: #3b4714;
    --badge-light: #c6d89a;
    --muted-light: #e6ebcf;
  }
  * { margin: 0; padding: 0; box-sizing: border-box; }
  html, body { width: 1200px; height: 784px; overflow: hidden; }
  body {
    position: relative;
    background: var(--page-bg);
    font-family: "Barlow Semi Condensed", "Arial Narrow", sans-serif;
    color: var(--ink);
  }
  .top-bar {
    position: absolute; left: 0; top: 0; width: 1200px; height: 46px;
    background: var(--olive-top);
  }
  .search {
    position: absolute; right: 36px; top: 14px;
    display: flex; align-items: center; gap: 8px;
    font-size: 13px; color: var(--muted-light); letter-spacing: .2px;
  }
  .main-nav {
    position: absolute; left: 0; top: 46px; width: 1200px; height: 76px;
    background: var(--nav-green);
  }
  .main-nav ul {
    list-style: none; position: absolute; right: 36px; top: 22px;
    display: flex; gap: 27px;
  }
  .main-nav a {
    font-size: 25px; font-weight: 600; letter-spacing: 1.4px;
    color: var(--ink); text-decoration: none; text-transform: uppercase;
  }
  .brand-badge {
    position: absolute; left: 24px; top: 22px; width: 258px; height: 258px;
    border-radius: 50%; background: var(--olive-dark);
    border: 6px solid var(--badge-light);
    display: flex; align-items: center; justify-content: center;
  }
  .brand-name {
    font-size: 44px; font-weight: 700; color: var(--badge-light);
    letter-spacing: 1px;
  }
  .photo {
    position: absolute; border: 2px solid #f1f2e6;
    box-shadow: 0 1px 4px rgba(0,0,0,.25);
  }
  .photo-tall {
    left: 316px; top: 160px; width: 226px; height: 298px;
    background: linear-gradient(160deg, #3a2a22 0%, #7a5a30 45%, #c89850 70%, #3b2a20 100%);
  }
  .photo-wide-small {
    left: 33px; top: 321px; width: 271px; height: 137px;
    background: linear-gradient(100deg, #1f3a2a 0%, #3e8a4a 35%, #4a5fa8 60%, #9a6a9a 85%, #2a2a30 100%);
  }
  .photo-shelf {
    left: 33px; top: 473px; width: 508px; height: 208px;
    background: linear-gradient(90deg, #c05a4a 0%, #d8a050 20%, #cfcfc8 45%, #8a8a88 70%, #b8b8b0 100%);
  }
  .about {
    position: absolute; left: 585px; top: 162px; width: 590px;
  }
  .about h1 {
    text-align: center; font-size: 86px; font-weight: 700;
    letter-spacing: 3px; line-height: 1; margin-left: -20px;
    margin-bottom: 36px;
  }
  .about p {
    font-size: 25px; font-weight: 600; line-height: 35px;
    letter-spacing: .4px; margin-bottom: 35px;
  }
  .site-footer {
    position: absolute; left: 0; top: 736px; width: 1200px; height: 48px;
    background: var(--olive-dark);
    font-size: 12px; color: var(--badge-light); letter-spacing: .4px;
  }
  .copyright { position: absolute; left: 24px; top: 19px; }
  .social { position: absolute; right: 24px; top: 9px; display: flex; align-items: center; gap: 12px; }
  .social-label { margin-right: 8px; }
  .social-dot { width: 28px; height: 28px; border-radius: 50%; background: var(--nav-green); }
</style>
</head>
<body>
  <header>
    <div class="top-bar">
      <div class="search">
        <svg width="13" height="13" viewBox="0 0 13 13" aria-hidden="true">
          <circle cx="5.2" cy="5.2" r="4" fill="none" stroke="#e6ebcf" stroke-width="1.6"/>
          <line x1="8.2" y1="8.2" x2="12" y2="12" stroke="#e6ebcf" stroke-width="1.8"/>
        </svg>
        <span>search for categories, brands &amp; products</span>
      </div>
    </div>
    <nav class="main-nav">
      <ul>
        <li><a href="#">Shop</a></li>
        <li><a href="#">About Us</a></li>
        <li><a href="#">Stores/Resellers</a></li>
        <li><a href="#">Brand Partners</a></li>
        <li><a href="#">Contact Us</a></li>
      </ul>
    </nav>
    <div class="brand-badge"><span class="brand-name">Birch Self</span></div>
  </header>

  <main>
    <div class="photo photo-tall" role="img" aria-label="Decorated glass water pipes lined up on a dark counter"></div>
    <div class="photo photo-wide-small" role="img" aria-label="Close-up of colourful glass pipes in green and blue"></div>
    <div class="photo photo-shelf" role="img" aria-label="Store shelves filled with rows of coloured glass pieces"></div>

    <section class="about">
      <h1>ABOUT US</h1>
      <p>We are multi-shop for marijuana-related accessories. We sell quality glass pipes, vaporizers, amazing storage options, dime bags, custom t-shirts and other stuff.</p>
      <p>We have a network of resellers that allow us to put in micro-installations into gift shops, convenience stores, tobacco stores, etc. and we are trying to change the overall perception that buying these items should be mainstream and as transparent as going to the Fen or the Walnut Shop.</p>
    </section>
  </main>

  <footer class="site-footer">
    <span class="copyright">2014 Run.Bake.Tend</span>
    <div class="social">
      <span class="social-label">social media</span>
      <span class="social-dot"></span>
      <span class="social-dot"></span>
      <span class="social-dot"></span>
      <span class="social-dot"></span>
    </div>
  </footer>
</body>
</html>
```